Simple but elegant business card/logo design for exclusive beauty business

We need a logo designed for a new elegant and exclusive beauty business called "G". The logo itself should be a stylistic and custom design for the letter "G". We would like the business card to have the logo as the centrepiece on a clean background. Gold Logo on black background or silver on white background.

The business card details should be displayed centre of the card. Details are as follows:

Tamsin Rowe
Facebook: /simplyshinebyr
Instagram: /simplyshinebyr

The words "Simply Shine" should also appear somewhere on the card.

G

• Design must be simple, clean and elegant
• The design should not be cluttered

```html
<!DOCTYPE html>
<html lang="en">
<head>
<meta charset="utf-8">
<title>Tamsin Rowe — Business Card</title>
<link rel="stylesheet" href="https://fonts.googleapis.com/css2?family=Playfair+Display:wght@700&display=swap">
<style>
  :root {
    --backdrop: #d7d7d7;
    --card: #2a2a2c;
    --card-deep: #222224;
    --gold: #c8b600;
    --gold-glow: rgba(200, 182, 0, 0.22);
  }
  * { margin: 0; padding: 0; box-sizing: border-box; }
  html, body {
    width: 1200px;
    height: 1041px;
    overflow: hidden;
    background: var(--backdrop);
  }
  .sheet {
    position: relative;
    width: 1200px;
    height: 1041px;
  }
  .card {
    position: absolute;
    left: 220px;
    width: 760px;
    height: 434px;
    background: radial-gradient(ellipse at 50% 40%, var(--card) 0%, var(--card-deep) 100%);
    box-shadow: 0 18px 40px rgba(0, 0, 0, 0.25);
    overflow: hidden;
    font-family: "Playfair Display", Georgia, serif;
    font-weight: 700;
    color: var(--gold);
  }
  .card--front { top: 46px; }
  .card--back { top: 561px; }
  .card__facets {
    position: absolute;
    inset: 0;
    width: 100%;
    height: 100%;
  }
  .card__content {
    position: absolute;
    inset: 0;
    display: flex;
    flex-direction: column;
    align-items: center;
    justify-content: center;
    text-align: center;
  }
  .brand-mark {
    display: flex;
    align-items: center;
    gap: 14px;
    font-size: 118px;
    line-height: 1;
  }
  .brand-mark__dot {
    width: 12px;
    height: 12px;
    border-radius: 50%;
    background: var(--gold);
  }
  .divider {
    width: 88px;
    height: 1.5px;
    background: var(--gold);
    margin: 14px 0 10px;
  }
  .tagline { font-size: 30px; letter-spacing: 0.5px; }
  .contact__name { font-size: 30px; }
  .contact__line { font-size: 30px; line-height: 1.2; }
</style>
</head>
<body>
<main class="sheet">

  <section class="card card--front" aria-label="Card front">
    <svg class="card__facets" viewBox="0 0 760 434" aria-hidden="true">
      <defs>
        <radialGradient id="glow-top" cx="0.5" cy="0" r="0.6">
          <stop offset="0" stop-color="var(--gold-glow)"/>
          <stop offset="1" stop-color="rgba(0,0,0,0)"/>
        </radialGradient>
      </defs>
      <polygon points="0,0 470,0 420,92 0,70" fill="url(#glow-top)"/>
      <polygon points="470,434 760,290 760,434" fill="url(#glow-top)" transform="rotate(180 615 362)"/>
      <g stroke="var(--gold)" stroke-width="1.5" fill="none">
        <line x1="0" y1="70" x2="470" y2="0"/>
        <line x1="150" y1="0" x2="40" y2="434"/>
        <line x1="330" y1="434" x2="760" y2="230"/>
        <line x1="560" y1="434" x2="760" y2="330"/>
      </g>
    </svg>
    <div class="card__content">
      <div class="brand-mark"><span class="brand-mark__dot"></span><span>R</span></div>
      <span class="divider"></span>
      <p class="tagline">Simply Shine</p>
    </div>
  </section>

  <section class="card card--back" aria-label="Card back">
    <svg class="card__facets" viewBox="0 0 760 434" aria-hidden="true">
      <defs>
        <radialGradient id="glow-band" cx="0.5" cy="0" r="0.7">
          <stop offset="0" stop-color="var(--gold-glow)"/>
          <stop offset="1" stop-color="rgba(0,0,0,0)"/>
        </radialGradient>
      </defs>
      <polygon points="0,0 420,0 0,150" fill="url(#glow-band)"/>
      <polygon points="90,320 760,380 760,434 0,434" fill="url(#glow-band)"/>
      <g stroke="var(--gold)" stroke-width="1.5" fill="none">
        <line x1="0" y1="150" x2="420" y2="0"/>
        <line x1="90" y1="320" x2="760" y2="380"/>
      </g>
    </svg>
    <div class="card__content">
      <p class="contact__name">Tamsin Rowe</p>
      <span class="divider"></span>
      <p class="contact__line">Facebook: /simplyshinebyr</p>
      <p class="contact__line">Instagram: /simplyshinebyr</p>
    </div>
  </section>

</main>
</body>
</html>
```